MD Business Card

I want to create a simple business card.
I am a consultant. I design and develop furniture, lighting and accessories for hospitality and retail brands.
I want the card to be simple and clean. Not too much of a logo - but it needs the basic information shown on the attached file.
Also - I have shown some fonts that I like on the attached file.
The card can be square or rectangle. It should be double sided.
I prefer 1-2 colors (not too colorful - but using color an an accent) Even if using color on the edges as an accent.

My snapquilt link shows some other graphics styles that I like. I like clean and simple.
http://www.snapquilt.com/marendowsett/business-cards/

Reason: I needed a few more days to see some of the options evolve.

Hospitality

```html
<!DOCTYPE html>
<html lang="en">
<head>
<meta charset="utf-8">
<title>MD Business Card</title>
<link rel="stylesheet" href="https://fonts.googleapis.com/css2?family=Ubuntu:wght@400&family=Michroma&display=swap">
<style>
:root{
  --accent:#5b93cf;
  --ink:#111111;
  --paper:#ffffff;
  --backdrop:#e9e9e6;
  --muted:#2a2a2a;
}
*{box-sizing:border-box;margin:0;padding:0}
html,body{width:1200px;height:792px;overflow:hidden}
body{background:var(--backdrop);position:relative;font-family:"Ubuntu",sans-serif}
.card{position:absolute;top:241px;width:540px;height:310px;overflow:hidden;box-shadow:0 6px 18px rgba(0,0,0,.18)}
.card--back{left:40px;background:var(--ink)}
.card--front{left:620px;background:var(--paper)}
.card svg{position:absolute;inset:0}
.brand{position:absolute;display:flex;align-items:center;gap:10px;color:var(--ink);white-space:nowrap}
.brand__mark{width:12px;height:12px;background:var(--ink);flex:none}
.brand__name{font-family:"Ubuntu",sans-serif;font-weight:400;font-size:30px;line-height:1}
.card--back .brand{left:212px;top:86px}
.card--front .brand{left:80px;top:128px}
.card--front .brand__mark{background:var(--accent)}
.person{position:absolute;right:64px;top:80px;text-align:right}
.person__name{font-family:"Michroma",sans-serif;font-size:15px;color:var(--accent);letter-spacing:1px}
.person__role{font-family:"Michroma",sans-serif;font-size:7px;color:var(--muted);letter-spacing:1px;margin-top:4px}
.contacts{position:absolute;right:42px;top:150px;list-style:none}
.contact{display:flex;justify-content:flex-end;align-items:center;gap:8px;height:22px;font-family:"Michroma",sans-serif;font-size:7px;color:var(--muted);white-space:nowrap}
.contact__icon{width:14px;height:14px;background:var(--accent);border-radius:2px;display:flex;align-items:center;justify-content:center;flex:none}
.contact__icon svg{position:static;width:9px;height:9px}
</style>
</head>
<body>
<section class="card card--back" aria-label="Card back">
  <svg viewBox="0 0 540 310" width="540" height="310" aria-hidden="true">
    <polygon points="50,0 540,0 540,225 230,225" fill="var(--accent)"/>
    <polygon points="68,8 532,8 532,217 236,217" fill="none" stroke="var(--ink)" stroke-width="1.5"/>
  </svg>
  <div class="brand">
    <span class="brand__mark"></span>
    <span class="brand__name">Maren Dowsett</span>
  </div>
</section>

<section class="card card--front" aria-label="Card front">
  <svg viewBox="0 0 540 310" width="540" height="310" aria-hidden="true">
    <polygon points="54,92 62,92 62,196 170,196 176,204 54,204" fill="var(--accent)"/>
    <polygon points="386,62 494,62 494,182 486,182 486,70 392,70" fill="var(--ink)"/>
  </svg>
  <div class="brand">
    <span class="brand__mark"></span>
    <span class="brand__name">Maren Dowsett</span>
  </div>
  <div class="person">
    <div class="person__name">REID CALLOWAY</div>
    <div class="person__role">GENERAL MANAGER</div>
  </div>
  <ul class="contacts">
    <li class="contact"><span>014 555 0123</span><span class="contact__icon"><svg viewBox="0 0 10 10"><path d="M2 1l2 2-1 1c.5 1 1.5 2 3 3l1-1 2 2-1.5 1.5C4 9 1 6 .5 2.5z" fill="#fff"/></svg></span></li>
    <li class="contact"><span>014 555 0124</span><span class="contact__icon"><svg viewBox="0 0 10 10"><rect x="2.5" y=".5" width="5" height="9" rx="1" fill="none" stroke="#fff"/></svg></span></li>
    <li class="contact"><span>reid@mailbox.test</span><span class="contact__icon"><svg viewBox="0 0 10 10"><rect x=".5" y="2" width="9" height="6" fill="none" stroke="#fff"/><path d="M.5 2l4.5 3.5L9.5 2" fill="none" stroke="#fff"/></svg></span></li>
    <li class="contact"><span>www.studiosite.test</span><span class="contact__icon"><svg viewBox="0 0 10 10"><circle cx="5" cy="5" r="4" fill="none" stroke="#fff"/><path d="M1 5h8M5 1c-2 2.5-2 5.5 0 8M5 1c2 2.5 2 5.5 0 8" fill="none" stroke="#fff" stroke-width=".8"/></svg></span></li>
    <li class="contact"><span>041 9th Floor Harbour Lane Road KTS</span><span class="contact__icon"><svg viewBox="0 0 10 10"><path d="M5 9.5C3 7 1.8 5.3 1.8 3.7a3.2 3.2 0 016.4 0C8.2 5.3 7 7 5 9.5z" fill="#fff"/><circle cx="5" cy="3.7" r="1.2" fill="var(--accent)"/></svg></span></li>
  </ul>
</section>
</body>
</html>
```